Quillmere Financial Plans

I am looking for a complete resdesign of my small financial presentation. This is a Word Doc/PDF that I print off when meeting with people in private. I often present my "two pager" that I have been using for years and years. It tells them the basics of what I do, how I help people and foundational financial principles.

I have recently gone out on my own in business and have completely rebranded. This presentation is my most used tool, so it is the first of many things I would like to redo. I am hoping it will somehow coordinate with the colors of my business, not necessarily the EXACT same 3 colors everywhere, but have the design colors compliment.

I've uploaded all my logo designs, as well as the current "two-pager". I am not against it going to 3 pages if needed. As it will still land on 2 pages with duplex printing.

It has always been VERY simple. I am wanting it built into a more professional and design specific format, to show off my branding, without being over cluttered.

I am completely open to ANY graphics changes. Obviously some are very novice, the house on the last page has always been overly simplified.

```html
<!DOCTYPE html>
<html lang="en">
<head>
<meta charset="utf-8">
<title>Quillmere Financial Plans – Two Pager</title>
<link href="https://fonts.googleapis.com/css2?family=Montserrat:wght@400;500;600;700;800&display=swap" rel="stylesheet">
<style>
:root{
  --navy:#0f2633;
  --navy-2:#1f3441;
  --green:#1fae4b;
  --red:#e8201f;
  --grey:#8d9396;
  --grey-light:#f1f1f1;
  --grey-soft:#ececec;
  --canvas:#ececec;
  --white:#ffffff;
}
*{box-sizing:border-box;margin:0;padding:0}
html,body{width:952px;height:1200px;overflow:hidden;background:var(--canvas);font-family:'Montserrat',sans-serif;color:var(--navy)}
.page{position:absolute;width:684px;height:988px;background:var(--white);transform:scale(.5567);transform-origin:top left;overflow:hidden}
.page-opt1{left:78px;top:35px}
.page-opt2{left:493px;top:35px}
.page-two{left:286px;top:615px;height:990px}
.abs{position:absolute}

.option-tag{position:absolute;left:293px;top:0;width:98px;height:27px;background:var(--red);color:var(--white);font-weight:800;font-size:15px;display:flex;align-items:center;justify-content:center;letter-spacing:.3px}
.corner-pattern{position:absolute;right:0;top:0;width:144px;height:110px;background:linear-gradient(225deg,rgba(31,174,75,.55),rgba(15,38,51,.12) 55%,rgba(255,255,255,0) 80%);clip-path:polygon(0 0,100% 0,100% 100%)}

.brand{position:absolute;left:46px;top:25px;color:var(--navy);font-weight:600;text-align:center}
.brand-name{font-size:22px;letter-spacing:.5px;line-height:1}
.brand-sub{font-size:7.5px;letter-spacing:1.6px;margin-top:4px;border-top:1px solid var(--navy);padding-top:2px}

.heading{position:absolute;font-weight:800;font-size:20.5px;line-height:23px;color:var(--navy)}
.heading .accent{color:var(--green);display:block}

.stat-card{position:absolute;left:45px;width:221px;border-radius:12px;background:linear-gradient(160deg,#34495a,#18303d 70%);color:var(--white);padding:12px 9px 0 16px;font-size:11px;line-height:13px;letter-spacing:-.35px;overflow:hidden}
.stat-card b{font-weight:800}
.stat-title{display:flex;align-items:center;gap:8px;font-size:19px;font-weight:700;margin-bottom:8px;line-height:1;letter-spacing:0}
.ring{width:38px;height:38px;border-radius:50%;background:var(--white);border:3px solid var(--green);box-shadow:inset 0 0 0 6px var(--white),inset 0 0 0 7.5px var(--navy);flex:none}
.source{display:inline-block;background:var(--green);color:var(--white);font-weight:700;font-size:9px;line-height:11px;letter-spacing:0;border-radius:9px;padding:2px 8px;margin:4px 0 10px}

.step{position:absolute;width:113px;background:var(--grey-light);border-radius:10px;text-align:center;font-weight:700;font-size:10px;line-height:11.5px}
.step-head{background:var(--navy);color:var(--white);border-radius:10px 10px 0 0;height:55px;display:flex;align-items:flex-end;justify-content:center;padding-bottom:7px;font-weight:800}
.step-icon{position:absolute;left:50%;top:-13px;width:28px;height:28px;margin-left:-14px;border-radius:50%;background:var(--white);border:2.5px solid var(--green)}
.step-body{padding-top:9px}
.down{display:block;width:0;height:0;margin:6px auto;border-left:6px solid transparent;border-right:6px solid transparent;border-top:8px solid var(--green)}
.split{display:flex;justify-content:space-around;font-size:9px;line-height:10px}
.right-arrow{position:absolute;width:0;height:0;border-top:6px solid transparent;border-bottom:6px solid transparent;border-left:8px solid var(--green)}

.pill{position:absolute;height:35px;border-radius:18px;background:var(--grey);color:var(--white);font-size:9.5px;font-weight:700;line-height:11px;display:flex;align-items:center;gap:8px;padding-left:6px}
.pill .ring{width:24px;height:24px;border-width:2px;box-shadow:inset 0 0 0 4px var(--white),inset 0 0 0 5px var(--grey)}
.arc-label{position:absolute;font-size:9.5px;font-weight:700;line-height:11px;color:var(--navy)}

.partner{position:absolute;width:86px;height:38px;background:var(--grey-light);border-radius:6px;display:flex;align-items:center;justify-content:center;font-size:9px;font-weight:600;color:var(--navy);text-align:center;line-height:10px}

.footer-band{position:absolute;left:0;bottom:0;width:100%;height:32px;background:linear-gradient(90deg,var(--navy) 40%,#0d6a33 80%,var(--green));color:var(--white);font-size:11px;font-weight:500;display:flex;align-items:center;justify-content:flex-end;gap:8px;padding-right:20px}
.page-num{width:18px;height:18px;border:1.5px solid var(--white);border-radius:50%;display:flex;align-items:center;justify-content:center;font-size:10px}

/* page two */
.top-zone{position:absolute;left:0;top:0;width:100%;height:412px;background:#f3f3f3}
.rate-table{position:absolute;top:132px;width:143px;font-size:13px}
.rate-head{display:flex;height:36px;color:var(--white);font-weight:800;font-size:15px}
.rate-head span{flex:1;display:flex;align-items:center;justify-content:center}
.rate-head .age{background:var(--navy)}
.rate-head .pct{background:var(--green)}
.rate-row{display:flex;height:25px;border-bottom:1px solid #9aa0a3}
.rate-row span{flex:1;display:flex;align-items:center;justify-content:center}
.rate-table.first .rate-row span:first-child{font-weight:800}
.doubles{position:absolute;top:340px;display:flex;align-items:center;gap:8px;font-weight:800;font-size:12px;line-height:12px}
.doubles .cash{width:40px;height:30px;border:2px solid var(--navy);border-radius:4px;background:linear-gradient(90deg,transparent 60%,rgba(31,174,75,.35) 60%)}
.doubles .green{color:var(--green);font-size:15px;line-height:14px}

.roof{position:absolute;left:44px;top:443px}
.struct-row{position:absolute;left:75px;width:530px;height:60px;display:flex;background:var(--grey-soft)}
.struct-name{width:176px;height:100%;display:flex;align-items:center;gap:12px;padding-left:14px;color:var(--white);font-weight:800;font-size:17px;position:relative}
.struct-name.navy{background:var(--navy)}
.struct-name.green{background:var(--green)}
.struct-name .ring{width:34px;height:34px;border-width:2.5px}
.struct-items{flex:1;display:grid;grid-template-columns:152px 130px;align-content:center;row-gap:4px;padding-left:14px;font-size:9.5px;font-weight:700;line-height:10.5px}
.check{display:flex;gap:5px;align-items:flex-start}
.check i{flex:none;width:11px;height:11px;border:1.3px solid var(--green);border-radius:50%;position:relative}
.check i::after{content:"";position:absolute;left:3px;top:1px;width:3px;height:5px;border:solid var(--green);border-width:0 1.3px 1.3px 0;transform:rotate(45deg)}
.tax-tag{align-self:center;width:41px;height:30px;background:var(--red);color:var(--white);border-radius:10px 0 0 10px;font-size:8.5px;font-weight:800;display:flex;align-items:center;justify-content:center;text-align:center;line-height:10px}
.foundation{position:absolute;left:51px;top:834px;width:583px;height:50px;border-radius:25px;background:var(--grey);color:var(--white);font-size:10px;font-weight:700;display:grid;grid-template-columns:1fr 1fr;padding:6px 44px;text-align:center;line-height:19px}
.foundation div:nth-child(-n+2){border-bottom:1px solid rgba(255,255,255,.6)}
.no-fund{position:absolute;left:300px;top:893px;display:flex;align-items:center;gap:6px;font-weight:800;font-size:13px;color:var(--navy)}
.no-fund .dot{width:26px;height:26px;border-radius:50%;border:3.5px solid var(--red)}
</style>
</head>
<body>

<!-- ============ OPTION 1 ============ -->
<section class="page page-opt1">
  <div class="option-tag">OPTION 1</div>
  <div class="corner-pattern" role="img" aria-label="Decorative green and grey triangle pattern"></div>
  <div class="brand"><div class="brand-name">QUILLMERE</div><div class="brand-sub">FINANCIAL PLANS</div></div>

  <h2 class="heading" style="left:44px;top:84px">THE FINANCIAL<span class="accent">CHALLENGE</span></h2>
  <h2 class="heading" style="left:284px;top:84px">FACING<span class="accent">THE CHALLENGE</span></h2>

  <article class="stat-card" style="top:141px;height:238px">
    <div class="stat-title"><span class="ring"></span>SAVINGS</div>
    <p><b>49%</b> of canadian employees are living paycheque to paycheque. <b>25%</b> of canadians are unable to cover an unexpected <b>$500</b> expense</p>
    <span class="source">Tallyline Stats (feb 2023)</span>
    <p><b>25%</b> of canadians need to access their retirement savings early. <b>20%</b> of canadians have no savings. 39% of canadians aged 55-65 have less than <b>$5,000</b> in savings.</p>
    <span class="source">Civic Ledger Report (june 2023)</span>
  </article>
  <article class="stat-card" style="top:391px;height:240px">
    <div class="stat-title"><span class="ring"></span>DEBT</div>
    <p>The average canadian has <b>$22,131</b> in consumer debt. Which excludes mortgages.</p>
    <span class="source">Crestmark Credit (aug 2024)</span>
    <p>Over <b>55%</b> of canadians hold credit card debt and the total canadian household debt has increased to <b>$2.52trillion</b>, including consumer credit, mortgage and non-mortgage loans.</p>
    <span class="source">Lenders Forum (aug 2024)</span>
  </article>
  <article class="stat-card" style="top:643px;height:260px">
    <div class="stat-title"><span class="ring"></span>INSURANCE</div>
    <p><b>45%</b> of canadians do not have individual life insurance coverage, but <b>48%</b> say their families would face financial trouble within 6 months of losing someone.</p>
    <span class="source">Veritas Risk Intl. (apr 2023)</span>
    <p>2-in-5 canadians (<b>43%</b> women / <b>44%</b> men) will be diagosed with a form of cancer or other critical illness during their lifetime. Every 7 seconds.</p>
    <span class="source">Wellstat Data (june 2024)</span>
  </article>

  <div class="step" style="left:282px;top:155px;height:146px"><span class="step-icon"></span><div class="step-head">CASH<br>FLOW</div><div class="step-body">ANALYSZE<br><br>FREE UP<br><br><span style="font-size:9px">$400<br>$600</span></div></div>
  <div class="right-arrow" style="left:398px;top:180px"></div>
  <div class="step" style="left:408px;top:155px;height:146px"><span class="step-icon"></span><div class="step-head">CASH FLOW<br>PROTECTION</div><div class="step-body">INCOME<br>PROTECTION<div class="split"><span class="down" style="margin:4px 0"></span><span class="down" style="margin:4px 0"></span></div><div class="split"><span>Life<br>Insurance</span><span>CI/DI<br>Insurance</span></div></div></div>
  <div class="step" style="left:534px;top:155px;height:146px"><span class="step-icon"></span><div class="step-head">DEBT<br>MANAGEMENT</div><div class="step-body" style="padding-top:13px">20%<span class="down"></span>6%-7%</div></div>

  <div class="step" style="left:282px;top:328px;height:147px"><span class="step-icon"></span><div class="step-head">EMERGENCY<br>FUND</div><div class="step-body">IF/ WHEN<span class="down"></span>3/6<br>Months</div></div>
  <div class="step" style="left:408px;top:328px;height:147px"><span class="step-icon"></span><div class="step-head">BUILD<br>WEALTH</div><div class="step-body">FINANCIAL<br>INDEPENDENCE<br>NUMBER<br>(F.I.N)</div></div>
  <div class="step" style="left:534px;top:328px;height:147px"><span class="step-icon"></span><div class="step-head">RESERVE<br>WEALTH</div><div class="step-body">LEAVING<br>A LEGACY<br><br><br>Will Prep</div></div>

  <h2 class="heading" style="left:284px;top:506px">HOW<span class="accent">WE WILL DO IT</span></h2>

  <svg class="abs" style="left:296px;top:565px" width="170" height="170" viewBox="-85 -85 170 170" role="img" aria-label="Pie chart of income: living expenses, taxes, savings and debt">
    <g stroke="#fff" stroke-width="2">
      <path d="M0,0 L0,82 A82,82 0 0 1 0,-82 Z" fill="#0f2633"/>
      <path d="M0,0 L0,-82 A82,82 0 0 1 76,-30.7 Z" fill="#0f2633"/>
      <path d="M0,0 L76,-30.7 A82,82 0 0 1 77.1,28 Z" fill="#a9adb0"/>
      <path d="M0,0 L77.1,28 A82,82 0 0 1 0,82 Z" fill="#1fae4b"/>
    </g>
    <g fill="#fff" font-family="Montserrat,sans-serif" font-weight="700" font-size="10.5" text-anchor="middle">
      <text x="-40" y="14">Living</text><text x="-40" y="27">Expenses</text>
      <text x="26" y="-26">Taxes</text>
      <text x="54" y="3">SAVINGS</text>
      <text x="26" y="56">Debt</text>
    </g>
  </svg>
  <div class="right-arrow" style="left:473px;top:643px"></div>
  <svg class="abs" style="left:470px;top:585px" width="30" height="130"><path d="M8,2 Q28,64 8,126" fill="none" stroke="#8d9396" stroke-dasharray="2 4"/></svg>
  <div class="pill" style="left:485px;top:570px;width:130px"><span class="ring"></span>RETIREMENT<br>SAVINGS</div>
  <div class="pill" style="left:508px;top:610px;width:126px"><span class="ring"></span>PROPER<br>PROTECTION</div>
  <div class="pill" style="left:508px;top:652px;width:126px"><span class="ring"></span>CHILDRREN'S<br>EDUCATION</div>
  <div class="pill" style="left:485px;top:694px;width:130px"><span class="ring"></span>FREEDOM<br>FROM DEBT</div>
  <svg class="abs" style="left:424px;top:740px" width="90" height="14"><line x1="0" y1="6" x2="30" y2="6" stroke="#8d9396"/><line x1="60" y1="6" x2="90" y2="6" stroke="#8d9396"/><path d="M38,1 L52,1 L45,12 Z" fill="#1fae4b"/></svg>

  <div class="partner" style="left:284px;top:764px">Harbourline</div>
  <div class="partner" style="left:379px;top:764px">Maplecrest Life</div>
  <div class="partner" style="left:471px;top:764px">Brightwell Life</div>
  <div class="partner" style="left:562px;top:764px">Kestrel Wealth</div>
  <div class="partner" style="left:284px;top:809px">Arbor Group</div>
  <div class="partner" style="left:379px;top:809px">Royalton Insurance</div>
  <div class="partner" style="left:471px;top:809px">Verana</div>
  <div class="partner" style="left:562px;top:809px">Bastion Insurance</div>
  <div class="partner" style="left:331px;top:853px">Neatfolio</div>
  <div class="partner" style="left:422px;top:853px">Fairway Life</div>
  <div class="partner" style="left:515px;top:853px">Ovanti</div>

  <footer class="footer-band">©QUILLMERE | FINANCIAL PLANS <span class="page-num">1</span></footer>
</section>

<!-- ============ OPTION 2 ============ -->
<section class="page page-opt2">
  <div class="option-tag">OPTION 2</div>
  <div class="corner-pattern" role="img" aria-label="Decorative green and grey triangle pattern"></div>
  <div class="brand"><div class="brand-name">QUILLMERE</div><div class="brand-sub">FINANCIAL PLANS</div></div>

  <h2 class="heading" style="left:44px;top:84px">THE FINANCIAL<span class="accent">CHALLENGE</span></h2>
  <h2 class="heading" style="left:284px;top:84px">FACING<span class="accent">THE CHALLENGE</span></h2>

  <article class="stat-card" style="top:141px;height:238px">
    <div class="stat-title"><span class="ring"></span>SAVINGS</div>
    <p><b>49%</b> of canadian employees are living paycheque to paycheque. <b>25%</b> of canadians are unable to cover an unexpected <b>$500</b> expense</p>
    <span class="source">Tallyline Stats (feb 2023)</span>
    <p><b>25%</b> of canadians need to access their retirement savings early. <b>20%</b> of canadians have no savings. 39% of canadians aged 55-65 have less than <b>$5,000</b> in savings.</p>
    <span class="source">Civic Ledger Report (june 2023)</span>
  </article>
  <article class="stat-card" style="top:391px;height:240px">
    <div class="stat-title"><span class="ring"></span>DEBT</div>
    <p>The average canadian has <b>$22,131</b> in consumer debt. Which excludes mortgages.</p>
    <span class="source">Crestmark Credit (aug 2024)</span>
    <p>Over <b>55%</b> of canadians hold credit card debt and the total canadian household debt has increased to <b>$2.52trillion</b>, including consumer credit, mortgage and non-mortgage loans.</p>
    <span class="source">Lenders Forum (aug 2024)</span>
  </article>
  <article class="stat-card" style="top:643px;height:260px">
    <div class="stat-title"><span class="ring"></span>INSURANCE</div>
    <p><b>45%</b> of canadians do not have individual life insurance coverage, but <b>48%</b> say their families would face financial trouble within 6 months of losing someone.</p>
    <span class="source">Veritas Risk Intl. (apr 2023)</span>
    <p>2-in-5 canadians (<b>43%</b> women / <b>44%</b> men) will be diagosed with a form of cancer or other critical illness during their lifetime. Every 7 seconds.</p>
    <span class="source">Wellstat Data (june 2024)</span>
  </article>

  <div class="step" style="left:282px;top:155px;height:146px"><span class="step-icon"></span><div class="step-head">CASH<br>FLOW</div><div class="step-body">ANALYSZE<br><br>FREE UP<br><br><span style="font-size:9px">$400<br>$600</span></div></div>
  <div class="right-arrow" style="left:398px;top:180px"></div>
  <div class="step" style="left:408px;top:155px;height:146px"><span class="step-icon"></span><div class="step-head">CASH FLOW<br>PROTECTION</div><div class="step-body">INCOME<br>PROTECTION<div class="split"><span class="down" style="margin:4px 0"></span><span class="down" style="margin:4px 0"></span></div><div class="split"><span>Life<br>Insurance</span><span>CI/DI<br>Insurance</span></div></div></div>
  <div class="step" style="left:534px;top:155px;height:146px"><span class="step-icon"></span><div class="step-head">DEBT<br>MANAGEMENT</div><div class="step-body" style="padding-top:13px">20%<span class="down"></span>6%-7%</div></div>

  <div class="step" style="left:282px;top:328px;height:147px"><span class="step-icon"></span><div class="step-head">EMERGENCY<br>FUND</div><div class="step-body">IF/ WHEN<span class="down"></span>3/6<br>Months</div></div>
  <div class="step" style="left:408px;top:328px;height:147px"><span class="step-icon"></span><div class="step-head">BUILD<br>WEALTH</div><div class="step-body">FINANCIAL<br>INDEPENDENCE<br>NUMBER<br>(F.I.N)</div></div>
  <div class="step" style="left:534px;top:328px;height:147px"><span class="step-icon"></span><div class="step-head">RESERVE<br>WEALTH</div><div class="step-body">LEAVING<br>A LEGACY<br><br><br>Will Prep</div></div>

  <h2 class="heading" style="left:284px;top:506px">HOW<span class="accent">WE WILL DO IT</span></h2>

  <svg class="abs" style="left:296px;top:565px" width="170" height="170" viewBox="-85 -85 170 170" role="img" aria-label="Pie chart of income: living expenses, taxes, savings and debt">
    <g stroke="#fff" stroke-width="2">
      <path d="M0,0 L0,82 A82,82 0 0 1 0,-82 Z" fill="#0f2633"/>
      <path d="M0,0 L0,-82 A82,82 0 0 1 76,-30.7 Z" fill="#0f2633"/>
      <path d="M0,0 L76,-30.7 A82,82 0 0 1 77.1,28 Z" fill="#a9adb0"/>
      <path d="M0,0 L77.1,28 A82,82 0 0 1 0,82 Z" fill="#1fae4b"/>
    </g>
    <g fill="#fff" font-family="Montserrat,sans-serif" font-weight="700" font-size="10.5" text-anchor="middle">
      <text x="-40" y="14">Living</text><text x="-40" y="27">Expenses</text>
      <text x="26" y="-26">Taxes</text>
      <text x="54" y="3">SAVINGS</text>
      <text x="26" y="56">Debt</text>
    </g>
  </svg>
  <svg class="abs" style="left:470px;top:555px" width="110" height="190" viewBox="0 0 110 190">
    <line x1="14" y1="55" x2="14" y2="80" stroke="#8d9396"/>
    <line x1="14" y1="110" x2="14" y2="135" stroke="#8d9396"/>
    <path d="M12,89 L22,95 L12,101 Z" fill="#1fae4b"/>
    <path d="M20,15 A80,80 0 0 1 20,175" fill="none" stroke="#8d9396" stroke-width="22"/>
    <g stroke="#fff" stroke-width="3">
      <line x1="69" y1="34" x2="85" y2="18"/>
      <line x1="89" y1="95" x2="112" y2="95"/>
      <line x1="69" y1="156" x2="85" y2="172"/>
    </g>
    <g fill="#fff" stroke="#8d9396" stroke-width="2">
      <circle cx="57" cy="24" r="10"/><circle cx="96" cy="68" r="10"/><circle cx="96" cy="122" r="10"/><circle cx="57" cy="166" r="10"/>
    </g>
  </svg>
  <div class="arc-label" style="left:544px;top:568px">RETIREMENT<br>SAVINGS</div>
  <div class="arc-label" style="left:579px;top:613px">PROPER<br>PROTECTION</div>
  <div class="arc-label" style="left:579px;top:670px">CHILDREN'S<br>EDUCATION</div>
  <div class="arc-label" style="left:544px;top:711px">FREEDOM<br>FROM DEBT</div>
  <svg class="abs" style="left:424px;top:740px" width="90" height="14"><line x1="0" y1="6" x2="30" y2="6" stroke="#8d9396"/><line x1="60" y1="6" x2="90" y2="6" stroke="#8d9396"/><path d="M38,1 L52,1 L45,12 Z" fill="#1fae4b"/></svg>

  <div class="partner" style="left:284px;top:764px">Harbourline</div>
  <div class="partner" style="left:379px;top:764px">Maplecrest Life</div>
  <div class="partner" style="left:471px;top:764px">Brightwell Life</div>
  <div class="partner" style="left:562px;top:764px">Kestrel Wealth</div>
  <div class="partner" style="left:284px;top:809px">Arbor Group</div>
  <div class="partner" style="left:379px;top:809px">Royalton Insurance</div>
  <div class="partner" style="left:471px;top:809px">Verana</div>
  <div class="partner" style="left:562px;top:809px">Bastion Insurance</div>
  <div class="partner" style="left:331px;top:853px">Neatfolio</div>
  <div class="partner" style="left:422px;top:853px">Fairway Life</div>
  <div class="partner" style="left:515px;top:853px">Ovanti</div>

  <footer class="footer-band">©QUILLMERE | FINANCIAL PLANS <span class="page-num">1</span></footer>
</section>

<!-- ============ PAGE 2 ============ -->
<section class="page page-two">
  <div class="top-zone"></div>
  <div class="corner-pattern" role="img" aria-label="Decorative green and grey triangle pattern"></div>
  <div class="brand"><div class="brand-name">QUILLMERE</div><div class="brand-sub">FINANCIAL PLANS</div></div>

  <h2 class="heading" style="left:44px;top:92px">RULE OF 72</h2>

  <div class="rate-table first" style="left:44px">
    <div class="rate-head"><span class="age">AGE</span><span class="pct">4%</span></div>
    <div class="rate-row"><span>29</span><span>$10,000</span></div>
    <div class="rate-row"><span>47</span><span>$20,000</span></div>
    <div class="rate-row"><span>65</span><span>$40,000</span></div>
  </div>
  <div class="rate-table" style="left:196px">
    <div class="rate-head"><span class="age">AGE</span><span class="pct">6%</span></div>
    <div class="rate-row"><span>29</span><span>$10,000</span></div>
    <div class="rate-row"><span>41</span><span>$20,000</span></div>
    <div class="rate-row"><span>53</span><span>$40,000</span></div>
    <div class="rate-row"><span>65</span><span>$80,000</span></div>
  </div>
  <div class="rate-table" style="left:345px">
    <div class="rate-head"><span class="age">AGE</span><span class="pct">8%</span></div>
    <div class="rate-row"><span>29</span><span>$10,000</span></div>
    <div class="rate-row"><span>38</span><span>$20,000</span></div>
    <div class="rate-row"><span>47</span><span>$40,000</span></div>
    <div class="rate-row"><span>56</span><span>$80,000</span></div>
    <div class="rate-row"><span>65</span><span>$160,000</span></div>
  </div>
  <div class="rate-table" style="left:494px">
    <div class="rate-head"><span class="age">AGE</span><span class="pct">12%</span></div>
    <div class="rate-row"><span>29</span><span>$10,000</span></div>
    <div class="rate-row"><span>35</span><span>$20,000</span></div>
    <div class="rate-row"><span>41</span><span>$40,000</span></div>
    <div class="rate-row"><span>47</span><span>$80,000</span></div>
    <div class="rate-row"><span>53</span><span>$160,000</span></div>
    <div class="rate-row"><span>59</span><span>$320,000</span></div>
  </div>

  <div class="doubles" style="left:58px"><span class="cash"></span><div>MONEY<br>DOUBLES<br><span class="green">EVERY<br>18 YEARS</span></div></div>
  <div class="doubles" style="left:210px"><span class="cash"></span><div>MONEY<br>DOUBLES<br><span class="green">EVERY<br>12 YEARS</span></div></div>
  <div class="doubles" style="left:359px"><span class="cash"></span><div>MONEY<br>DOUBLES<br><span class="green">EVERY<br>9 YEARS</span></div></div>
  <div class="doubles" style="left:508px"><span class="cash"></span><div>MONEY<br>DOUBLES<br><span class="green">EVERY<br>6 YEARS</span></div></div>

  <h2 class="heading" style="left:44px;top:428px">STRUCTURE</h2>
  <svg class="roof" width="597" height="112" viewBox="0 0 597 112">
    <path d="M289,0 L546,80 L51,80 Z" fill="#a8acae"/>
    <rect x="0" y="80" width="597" height="12" fill="#c8c9ca"/>
    <rect x="31" y="95" width="530" height="17" fill="#c4c5c6"/>
  </svg>

  <div class="struct-row" style="top:562px">
    <div class="struct-name navy"><span class="ring"></span>HOME</div>
    <div class="struct-items"><span class="check"><i></i>PARTNER WITH MORTGAGE BROKERS FOR BEST RATES</span><span class="check"><i></i>MORTGAGE INSURANCE ALTERNATIVES</span></div>
    <span class="tax-tag">SELL</span>
  </div>
  <div class="struct-row" style="top:629px">
    <div class="struct-name green"><span class="ring"></span>RRSP</div>
    <div class="struct-items"><span class="check"><i></i>TAX DEDUCTION</span><span></span><span class="check"><i></i>TAX DEFERRED</span></div>
    <span class="tax-tag">100%<br>TAX</span>
  </div>
  <div class="struct-row" style="top:695px">
    <div class="struct-name navy"><span class="ring"></span>TFSA</div>
    <div class="struct-items"><span class="check"><i></i>NO TAX DEDUCTIONS</span><span class="check"><i></i>2009-$102,000</span><span class="check"><i></i>TAX FREE GROWTH</span><span class="check"><i></i>2025 LIMIT - $7000/YR</span></div>
    <span class="tax-tag">0%<br>TAX</span>
  </div>
  <div class="struct-row" style="top:762px">
    <div class="struct-name green"><span class="ring"></span>PERM LIFE</div>
    <div class="struct-items"><span class="check"><i></i>NO TAX DEDUCTION</span><span class="check"><i></i>TAX DEFERRED GROWTH</span><span class="check"><i></i>QUALIFY</span></div>
    <span class="tax-tag">0%<br>TAX</span>
  </div>

  <div class="foundation">
    <div>EMERGENCY/OPPORTUNITY FUNDS</div><div>DEBT MANAGEMENT</div>
    <div>CASHFLOW PROTECTION (LI/CI/DI)</div><div>CASH FLOW</div>
  </div>

  <div class="no-fund"><span class="dot"></span>Fundbowl</div>

  <footer class="footer-band">©QUILLMERE | FINANCIAL PLANS <span class="page-num">2</span></footer>
</section>

</body>
</html>
```